Chiropractic healthcare group business card

We are a Portland Oregon based chiropractic healthcare group. Looking for a new business card design. Something cutting edge, that shows off our new logo and tag line.Use either of the attached logos.Our tag line = "Who would you be without pain?"I'm open to about anything, impress me!!
Target Market(s)
Chiropractic patients - Auto injury, back pain, sports injuries, neck , shoulder, hip, knee, ankle pain.
Industry/Entity Type
Chiropractic
Contact Information for Business Card
Dr. Bram Holtvick, D.C.
Clinic name - Fernway Chiropractic
2 clinics
location #1
20418 NW Marwick Road
Suite B
North Plains, OR 97133
Location #2
13529 SE Calloway Street
Portland OR 97236
Main phone line 971.555.0143
website : www.FernwayClinics.example
Tag line "Who would you be without pain?"
Colors
Designer to choose colors to be used in the design.
Requirements
Must have
- Use the logo colors -- Want the orange color to be a TRUE orange.
- Both clinic address
- phone number
- website
- personal email - b.holtvick@ReliefBeginsHere.example
- tag line - "Who would you be without pain?"

```html
<!DOCTYPE html>
<html lang="en">
<head>
<meta charset="utf-8">
<title>Fernway Chiropractic – Business Card</title>
<link rel="stylesheet" href="https://fonts.googleapis.com/css2?family=Open+Sans:wght@400;600;700&display=swap">
<style>
  :root {
    --backdrop: #646464;
    --card-dark: #6d6e6e;
    --card-light: #ffffff;
    --orange: #f2a533;
    --slate: #666768;
    --text: #5a5b5c;
  }
  * { box-sizing: border-box; margin: 0; padding: 0; }
  html, body { width: 1200px; height: 985px; overflow: hidden; }
  body {
    background: var(--backdrop);
    font-family: "Open Sans", sans-serif;
    position: relative;
  }
  .card {
    position: absolute;
    left: 250px;
    width: 700px;
    height: 400px;
    overflow: hidden;
    box-shadow: 0 6px 18px rgba(0,0,0,.25);
  }
  /* Back side */
  .card-back { top: 52px; background: var(--card-dark); }
  .card-back .brand {
    position: absolute; left: 0; right: 0; top: 130px;
    text-align: center; color: var(--card-light);
    font-weight: 700; font-size: 40px; letter-spacing: 12px; line-height: 1.25;
  }
  .card-back .tagline {
    position: absolute; left: 0; right: 0; top: 300px;
    text-align: center; color: var(--orange); font-size: 22px;
  }
  /* Front side */
  .card-front { top: 512px; background: var(--card-light); }
  .card-front .brand {
    position: absolute; left: 40px; top: 130px; width: 300px;
    text-align: center; color: var(--slate);
    font-weight: 700; font-size: 30px; letter-spacing: 7px; line-height: 1.3;
  }
  .divider {
    position: absolute; left: 360px; width: 4px;
  }
  .divider-top { top: 34px; height: 150px; background: var(--orange); }
  .divider-bottom { top: 190px; height: 170px; background: var(--slate); }
  .details { position: absolute; left: 386px; top: 30px; width: 300px; color: var(--text); }
  .doctor { color: var(--orange); font-weight: 700; font-size: 21px; margin-bottom: 6px; }
  .location-label { color: var(--orange); font-size: 17px; line-height: 1.2; }
  .address { font-size: 16px; line-height: 1.3; margin-bottom: 8px; }
  .contact { list-style: none; margin-top: 6px; font-size: 14px; }
  .contact li { display: flex; align-items: center; gap: 8px; line-height: 1.55; white-space: nowrap; }
  .contact svg { width: 16px; height: 16px; flex: none; }
  .contact .accent { color: var(--orange); }
  .band { position: absolute; bottom: 0; height: 16px; }
  .band-orange { left: 0; width: 390px; background: var(--orange); }
  .band-slate { left: 396px; right: 0; background: var(--slate); }
</style>
</head>
<body>

<section class="card card-back" aria-label="Card back">
  <div class="brand">FERNWAY<br>CHIROPRACTIC</div>
  <p class="tagline">“Who would you be without pain?”</p>
</section>

<section class="card card-front" aria-label="Card front">
  <div class="brand">FERNWAY<br>CHIROPRACTIC</div>

  <span class="divider divider-top"></span>
  <span class="divider divider-bottom"></span>

  <div class="details">
    <p class="doctor">Dr. BRAM HOLTVICK, D.C.</p>
    <p class="location-label">location #1</p>
    <p class="address">20418 NW Marwick Road, Suite B<br>North Plains, OR 97133</p>
    <p class="location-label">location #2</p>
    <p class="address">13529 SE Calloway Street<br>Portland OR 97236</p>
    <ul class="contact">
      <li>
        <svg viewBox="0 0 16 16" aria-hidden="true"><path fill="#f2a533" d="M4 1l2.5 3-1.5 2c.8 2 2.5 3.7 4.5 4.5l2-1.5 3 2.5-1.5 2.5C7.5 15 1 8.5 1.5 2.5z"/></svg>
        <span>971.555.0143</span>
      </li>
      <li>
        <svg viewBox="0 0 16 16" aria-hidden="true"><rect x="1" y="3" width="14" height="10" fill="#f2a533"/><path d="M1 3l7 6 7-6" fill="none" stroke="#fff" stroke-width="1.4"/></svg>
        <span>b.holtvick@ReliefBeginsHere.example</span>
      </li>
      <li>
        <svg viewBox="0 0 16 16" aria-hidden="true"><circle cx="8" cy="8" r="7" fill="#f2a533"/><path d="M1 8h14M8 1c-3 3.5-3 10.5 0 14M8 1c3 3.5 3 10.5 0 14" fill="none" stroke="#fff" stroke-width="1"/></svg>
        <span>www.<span class="accent">FernwayClinics</span>.example</span>
      </li>
    </ul>
  </div>

  <span class="band band-orange"></span>
  <span class="band band-slate"></span>
</section>

</body>
</html>
```